One of Australia's fastest growing Financial Company looking for an updated business card design!

Meridale Holdings Australia is looking for an updated design for our business cards. We would like to keep up our professional appearances and have get new exciting design that fits our company.

The Meridale aim is to facilitate and assist clients in every financial requirement that may arise in financial areas.

We would to see the design to use colour blue and we like the clouds in the background. We have attached two designs we have use before but we need something with more professional and easy to read design.

We would like the website in the back of the card; the employees name more central and stands out; only a postal address; a list of all our locations along the bottom (Sydney, Melbourne, Brisbane, Singapore)

Looking forward to seeing the designs come in!

Target Market(s)

Other Industry Professionals
Middle Class Families

Industry/Entity Type

Finance

Contact Information for Business Card

Name; Company Role; Office Number; Mobile Number; Email Address; Website; Postal Address; Locations

Font styles to use
Serif
Sans Serif

Colors
0492cd
33a6d7
85cae6
85acd3
3176b5
0455a3
cee9f5
d5e2ee

Requirements
Must have
• Name; Company Role; Office Number; Mobile Number; Email Address; Website; Postal Address; Locations
Nice to have
• The colour blue, clouds on the background

```html
<!DOCTYPE html>
<html lang="en">
<head>
<meta charset="utf-8">
<title>Meridale Holdings Australia – Business Card</title>
<link rel="stylesheet" href="https://fonts.googleapis.com/css2?family=Source+Sans+3:wght@400;600;700&display=swap">
<style>
  :root {
    --page-bg: #e4e6e8;
    --sky-deep: #2c68ad;
    --sky-mid: #3f82c4;
    --sky-light: #85acd3;
    --cloud: #cee9f5;
    --card-black: #0c0c0d;
    --card-charcoal: #1c1d1f;
    --brand-blue: #0492cd;
    --name-blue: #33a6d7;
    --accent-red: #e0393e;
    --text-white: #ffffff;
    --text-soft: #e6e6e6;
    --rule: #2b2c2f;
  }
  * { box-sizing: border-box; margin: 0; padding: 0; }
  html, body {
    width: 1200px; height: 900px; overflow: hidden;
    background: var(--page-bg);
    font-family: "Source Sans 3", "Segoe UI", Arial, sans-serif;
  }
  .canvas {
    position: relative; width: 1200px; height: 900px;
    display: flex; flex-direction: column; align-items: center; justify-content: center; gap: 56px;
  }
  .card {
    position: relative; width: 600px; height: 343px; overflow: hidden;
    box-shadow: 0 6px 18px rgba(0,0,0,.18);
  }

  /* Front */
  .card-front { background: var(--sky-mid); }
  .sky-backdrop {
    position: absolute; inset: 0;
    background:
      radial-gradient(ellipse 40% 30% at 70% 85%, rgba(206,233,245,.55), transparent 70%),
      radial-gradient(ellipse 35% 30% at 12% 60%, rgba(206,233,245,.4), transparent 70%),
      radial-gradient(ellipse 30% 25% at 95% 40%, rgba(206,233,245,.35), transparent 70%),
      radial-gradient(ellipse 60% 50% at 50% 40%, var(--sky-light), transparent 80%),
      linear-gradient(160deg, var(--sky-deep), var(--sky-mid) 55%, var(--sky-light));
  }
  .front-brand {
    position: absolute; left: 0; right: 0; top: 112px;
    display: flex; align-items: center; justify-content: center; gap: 14px;
  }
  .brand-dot { width: 22px; height: 22px; border-radius: 50%; background: var(--text-white); }
  .front-brand .brand-name {
    font-size: 68px; font-weight: 600; color: var(--text-white); letter-spacing: .5px; line-height: 1;
  }
  .website {
    position: absolute; left: 0; right: 0; top: 210px; text-align: center;
    font-size: 15px; color: var(--text-white); letter-spacing: .3px;
  }

  /* Back */
  .card-back {
    background: radial-gradient(ellipse 80% 70% at 55% 35%, var(--card-charcoal), var(--card-black));
    color: var(--text-white);
  }
  .person { position: absolute; left: 44px; top: 56px; }
  .person-name { font-size: 20px; font-weight: 700; color: var(--name-blue); }
  .person-role { font-size: 15px; color: var(--text-soft); margin-top: 2px; }
  .postal-address {
    position: absolute; left: 44px; top: 148px;
    font-size: 16px; line-height: 1.3; color: var(--text-soft); font-style: normal;
  }
  .back-brand {
    position: absolute; right: 44px; top: 62px;
    display: flex; align-items: center; gap: 12px;
  }
  .back-brand .brand-dot { background: var(--brand-blue); width: 20px; height: 20px; }
  .back-brand .brand-name { font-size: 62px; font-weight: 600; color: var(--brand-blue); line-height: 1; }
  .brand-rule {
    position: absolute; left: 300px; right: 44px; top: 150px; height: 1px; background: var(--rule);
  }
  .contacts {
    position: absolute; right: 30px; top: 200px; list-style: none;
    font-size: 16px; line-height: 1.4; color: var(--text-soft); text-align: right;
  }
  .contacts li { display: flex; align-items: center; justify-content: flex-end; gap: 8px; }
  .contacts svg { width: 12px; height: 12px; fill: var(--name-blue); }
  .locations {
    position: absolute; left: 0; right: 0; bottom: 34px; list-style: none;
    display: flex; justify-content: center; align-items: center;
    font-size: 17px; font-weight: 700; color: var(--text-white);
  }
  .locations li + li::before {
    content: ""; display: inline-block; width: 8px; height: 8px; border-radius: 50%;
    background: var(--accent-red); margin: 0 6px 2px; vertical-align: middle;
  }
</style>
</head>
<body>
<main class="canvas">
  <section class="card card-front" aria-label="Card front">
    <div class="sky-backdrop" role="img" aria-label="Blue sky with soft white clouds"></div>
    <div class="front-brand">
      <span class="brand-dot"></span>
      <span class="brand-name">Meridale</span>
    </div>
    <p class="website">www.meridaleholdings.com</p>
  </section>

  <section class="card card-back" aria-label="Card back">
    <div class="person">
      <p class="person-name">Daniel Carter</p>
      <p class="person-role">Managing Director</p>
    </div>
    <address class="postal-address">PO Box 4120, Sydney NSW 2001,<br>Australia</address>
    <div class="back-brand">
      <span class="brand-dot"></span>
      <span class="brand-name">Meridale</span>
    </div>
    <div class="brand-rule"></div>
    <ul class="contacts">
      <li>555.201.4830
        <svg viewBox="0 0 12 12" aria-label="Mobile"><path d="M3 0h6a1 1 0 0 1 1 1v10a1 1 0 0 1-1 1H3a1 1 0 0 1-1-1V1a1 1 0 0 1 1-1zm0 1.5v8h6v-8z"/></svg>
      </li>
      <li>555.201.4831
        <svg viewBox="0 0 12 12" aria-label="Office phone"><path d="M1 4c0-2 2-3 5-3s5 1 5 3v1H8V3.5H4V5H1zM2 6h8l1 5H1z"/></svg>
      </li>
      <li>info@meridaleholdings.com
        <svg viewBox="0 0 12 12" aria-label="Email"><path d="M0 2h12v8H0zm1 1v.3l5 3.2 5-3.2V3z"/></svg>
      </li>
    </ul>
    <ul class="locations">
      <li>Sydney</li>
      <li>Melbourne</li>
      <li>Brisbane</li>
      <li>Singapore</li>
    </ul>
  </section>
</main>
</body>
</html>
```